TRIVAN 2026 Flyer for Conference

TRIVAN needs a design for a 1-page flyer that we will hand out at an upcoming event & then later post online as a pdf. There are 3 elements which need to be on the flyer:

1) A logo. This should be prominent on the design (e.g., in the middle). The flyer should use the colors that are in that logo (e.g., for accents, design elements, and/or text; not all of these have to be used):
Dark blue: #185577
Med blue: #327C9A
Teal: #4EB1C2
Light Teal: #9EDBE6

2) The conference theme -- Forests of Wonder: Climbing toward Research Fluency -- should be at the flyer's top.

3) Finally, these six tracks should be listed below the theme and the logo (it's font size should be at least a couple sizes smaller than the size used for the theme):
- Pearls of Pedagogy: Teaching Techniques that Work
- The Depth Gauge: Measuring Instructional Impact
- Techtonic Shifts: Innovation and Educational Technology
- Captain's Log: Navigating Leadership in Library Instruction
- Swimming Together: Collaborating with Others
- The Bermuda Triangle: Exploring (Seemingly) Eternal Challenges

Font styles to use
Sans Serif

Colors
0094D4
00A9DD
6FCCEA
C7EBF8
E9F6FB

Requirements
Must have
• The 3 elements listed in the description: 1) the logo, 2) the text of the theme and 3) the text for the tracks.

```html
<!DOCTYPE html>
<html lang="en">
<head>
<meta charset="utf-8">
<title>TRIVAN 2026 – Forests of Wonder</title>
<link rel="stylesheet" href="https://fonts.googleapis.com/css2?family=Fredoka:wght@500;600;700&family=Arimo:wght@400&display=swap">
<style>
  :root {
    --dark-blue: #185577;
    --med-blue: #327C9A;
    --teal: #4EB1C2;
    --light-teal: #9EDBE6;
    --paper: #dcdcdc;
    --stage: #8f8e8e;
    --sea-deep: #2f5e62;
    --sea-mid: #5f8d8f;
    --sea-foam: #b9cfd0;
  }
  * { margin: 0; padding: 0; box-sizing: border-box; }
  html, body {
    width: 1199px;
    height: 1200px;
    overflow: hidden;
    background: var(--stage);
  }
  .flyer {
    position: absolute;
    left: 229px;
    top: 75px;
    width: 742px;
    height: 1050px;
    background: var(--paper);
    overflow: hidden;
    font-family: "Arimo", Arial, sans-serif;
  }
  .brand {
    position: absolute;
    top: 92px;
    left: 0;
    width: 100%;
    display: flex;
    justify-content: center;
    align-items: center;
    gap: 14px;
  }
  .brand-dot {
    width: 38px;
    height: 38px;
    border-radius: 50%;
    background: var(--teal);
  }
  .brand-name {
    font-family: "Fredoka", sans-serif;
    font-weight: 600;
    font-size: 54px;
    line-height: 1;
    color: var(--dark-blue);
  }
  .theme {
    position: absolute;
    top: 236px;
    left: 0;
    width: 100%;
    text-align: center;
    font-family: "Fredoka", sans-serif;
    font-weight: 700;
    text-transform: uppercase;
  }
  .theme-lead {
    display: block;
    font-size: 124px;
    line-height: 1;
    letter-spacing: 2px;
    color: var(--teal);
    text-shadow: 4px 5px 6px rgba(0,0,0,0.18);
  }
  .theme-joiner {
    display: block;
    font-size: 28px;
    line-height: 1;
    color: var(--dark-blue);
    text-align: right;
    padding-right: 150px;
    margin-top: -2px;
  }
  .theme-main {
    display: block;
    font-size: 78px;
    line-height: 1;
    letter-spacing: 1px;
    color: var(--dark-blue);
    text-shadow: 3px 4px 5px rgba(0,0,0,0.15);
  }
  .subtitle-band {
    position: absolute;
    top: 460px;
    left: 86px;
    width: 575px;
    height: 64px;
  }
  .subtitle-band svg {
    position: absolute;
    inset: 0;
  }
  .subtitle-text {
    position: absolute;
    inset: 0;
    display: flex;
    align-items: center;
    justify-content: center;
    font-family: "Fredoka", sans-serif;
    font-weight: 600;
    font-size: 25px;
    letter-spacing: 0.5px;
    color: var(--med-blue);
    text-transform: uppercase;
  }
  .tracks {
    position: absolute;
    top: 560px;
    left: 0;
    width: 100%;
    list-style: none;
    text-align: center;
    color: var(--dark-blue);
    font-size: 19px;
    line-height: 30px;
  }
  .sea {
    position: absolute;
    left: 0;
    bottom: 0;
    width: 100%;
    height: 310px;
    background:
      linear-gradient(180deg, var(--paper) 0%, #c9d2d2 6%, var(--sea-mid) 18%, var(--sea-deep) 40%, var(--sea-foam) 62%, var(--sea-mid) 78%, var(--sea-deep) 100%);
  }
</style>
</head>
<body>
  <main class="flyer">
    <div class="brand">
      <span class="brand-dot"></span>
      <span class="brand-name">TRIVAN 2026</span>
    </div>

    <h1 class="theme">
      <span class="theme-lead">Forests</span>
      <span class="theme-joiner">of</span>
      <span class="theme-main">Wonder:</span>
    </h1>

    <div class="subtitle-band">
      <svg width="575" height="64" viewBox="0 0 575 64" aria-hidden="true">
        <polygon points="0,0 575,10 560,64 12,56" fill="#9EDBE6"/>
      </svg>
      <p class="subtitle-text">Climbing toward Research Fluency</p>
    </div>

    <ul class="tracks">
      <li>Pearls of Pedagogy: Teaching Techniques that Work</li>
      <li>The Depth Gauge: Measuring Instructional Impact</li>
      <li>Techtonic Shifts: Innovation and Educational Technology</li>
      <li>Captain's Log: Navigating Leadership in Library Instruction</li>
      <li>Swimming Together: Collaborating with Others</li>
      <li>The Bermuda Triangle: Exploring (Seemingly) Eternal Challenges</li>
    </ul>

    <div class="sea" role="img" aria-label="Photograph of rough teal ocean waves breaking under a pale sky"></div>
  </main>
</body>
</html>
```